A Techincal Author needs a site to promote his Programming Books

The StudyAlong series is a collection of books focusing on building the same app with different technologies. The purpose of this project is to design a web site home page that can be used to sell the books.

Expected Deliverables
• StudyAlong Logo as Illustrator file
• Master graphic design files for any relevant web assets
• HTML and CSS for home page, if applicable

Target Market(s)

The target market for our series is web programmers. They are people who have some experience, but want to learn a new tool. Programmers are analytical, logical people who like structure in the things they do.

Here are some things our customers like:

• Chirpline / Postora
• Clan of Ravens / Hollow Marsh / Burning Low
• SmartPhones, Tablets, Stridelets, and other tech gadgets.

The design should try to speak to that market.

Industry/Entity Type

Building

Coding

Coded - Design and coding required

Number of Pages Required

1 page

Requirements
Must have
• The primary tasks for this project are:
• 1) Create "Study Along" Logo.
• * All “NetBrookly” properties use a similar logo approach, with the NetBrookly ball icon on the left, a reflection below it. The company name is on the right, roughly the same size as the ball icon. A tag line underneath the company name, roughly the same size as the reflection.
• * Company Name: Study Along
• * Tagline: Knowledge to Boost Your Career
• * Logo color is up to the discretion of the designer, but should be compatible with the site design.
• * Sample Logos for other NetBrookly properties in Illustrator format are available as attachments to this project.
• 2) Design the Study Along Home Page.
• The home page should follow this format:
• * Logo
• * Nav Bar
• • Buy (The Home Page)
• • About
• • Contact
• * Main Content
• • Home page content detailed in attachment
• * Footer
• • Copyright notice
• • Links to other stuff we do ( net-brook-ly.com | marlontrevick.com | PathPastGrid.com )
Nice to have
• It would be nice to have a book as part of the home page content.
Should not have
• Please do not use the same color scheme as PathPastGrid.com or Gridmora.com or QueryTheGridsmith.com

```html
<!DOCTYPE html>
<html lang="en">
<head>
<meta charset="utf-8">
<title>StudyAlong – Knowledge to Boost Your Career</title>
<link rel="stylesheet" href="https://fonts.googleapis.com/css2?family=Open+Sans:wght@300;400;600;700&family=Roboto:wght@400;500;700&display=swap">
<style>
:root{
  --orange:#ff7150;
  --orange-deep:#e4522c;
  --ink:#1e1f21;
  --text:#3a3a3a;
  --muted:#6b6b6b;
  --panel-bg:#efefef;
  --band:#e8e8e8;
  --line:#dcdcdc;
  --white:#ffffff;
  --display:'Open Sans',sans-serif;
  --body:'Roboto',sans-serif;
}
*{margin:0;padding:0;box-sizing:border-box}
html,body{width:786px;height:1200px;overflow:hidden}
body{position:relative;background:var(--white);font-family:var(--body);color:var(--text)}
.abs{position:absolute}

/* header */
.site-header{left:0;top:0;width:786px;height:72px;border-top:2px solid var(--orange);background:var(--white);border-bottom:1px solid #e6e6e6}
.brand-mark{left:74px;top:18px;width:26px;height:26px;border-radius:50%;background:var(--orange)}
.brand-name{left:105px;top:24px;font-family:var(--display);font-weight:600;font-size:20px;line-height:22px;color:#222}
.brand-tag{left:106px;top:50px;font-size:7px;color:var(--muted)}
.main-nav a{position:absolute;top:31px;font-family:var(--display);font-size:7.5px;font-weight:600;color:#444;text-decoration:none;padding-bottom:10px}
.main-nav a.active{color:var(--orange);border-bottom:2px solid var(--orange)}

/* hero */
.hero{left:0;top:72px;width:786px;height:269px;background:var(--orange)}
.hero-art{left:135px;top:10px;width:235px;height:259px;border-radius:50% 50% 8px 8px / 45% 45% 8px 8px;background:radial-gradient(circle at 50% 40%,#ffb27a 0%,#f7864f 55%,#ff7150 100%)}
.hero-title{left:396px;top:48px;font-family:var(--display);color:var(--white);line-height:1}
.hero-title .l1{display:block;font-size:39px;font-weight:400;letter-spacing:1px}
.hero-title .l2{display:block;font-size:32px;font-weight:400;margin-top:8px;letter-spacing:.5px}
.hero-title .l3{display:block;font-size:70px;font-weight:400;margin-top:4px;letter-spacing:1px}

/* signup */
.signup{left:0;top:341px;width:786px;height:156px;background:var(--ink)}
.signup h2{position:absolute;left:0;top:32px;width:786px;text-align:center;font-family:var(--display);font-weight:400;font-size:17px;color:var(--white)}
.field{top:77px;width:192px;height:36px;border:1px solid #d9d9d9;border-radius:2px;color:#cfcfcf;font-size:7px;padding:0 14px;display:flex;align-items:center}
.submit{left:541px;top:77px;width:123px;height:36px;border-radius:2px;background:linear-gradient(#f2683f,#c94720);color:var(--white);font-family:var(--display);font-size:13px;display:flex;align-items:center;justify-content:center}

/* books */
.catalog{left:0;top:497px;width:786px;height:371px;background:var(--panel-bg)}
.book-panel{left:72px;width:640px;background:#f7f7f7;border:1px solid #dedede;box-shadow:0 1px 2px rgba(0,0,0,.12)}
.panel-head{height:36px;display:flex;align-items:center;background:linear-gradient(#f8f8f8,#ececec);border-bottom:1px solid #dcdcdc}
.panel-toggle{width:33px;height:36px;border-right:1px solid #dcdcdc;display:flex;align-items:center;justify-content:center}
.panel-title{font-family:var(--display);font-size:12.5px;color:#4a4a4a;margin-left:13px;flex:1}
.app-link{display:flex;align-items:center;gap:4px;font-family:var(--display);font-size:7.5px;color:#555;margin-right:12px}
.price-table{position:absolute;left:14px;top:50px;width:612px;border-collapse:separate;border-spacing:0 2px;font-size:9px}
.price-table td{height:29px;background:var(--white);border-top:1px solid #e4e4e4;border-bottom:1px solid #e4e4e4;border-right:1px solid #e4e4e4;padding:0 13px}
.price-table td:first-child{border-left:1px solid #e4e4e4;color:var(--orange);width:193px}
.price-table .price{color:var(--orange);text-align:center;width:111px}
.price-table .store{text-align:center;color:#555}
.store-name{font-weight:700;color:#222;font-size:8px;margin-left:4px}
.store-dot{display:inline-block;width:9px;height:9px;border:1px solid var(--orange);border-radius:2px;vertical-align:-1px;margin-left:5px}

/* author */
.author{left:0;top:868px;width:786px;height:179px;background:var(--white)}
.author-photo{left:74px;top:34px;width:112px;height:112px;border-radius:50%;border:3px solid #e5e5e5;background:linear-gradient(#8a8a7e,#3a3834)}
.author-title{left:203px;top:39px;font-family:var(--display);font-size:14px;font-weight:400;color:#222}
.author-copy{left:203px;top:60px;width:505px;font-size:6.5px;line-height:20px;color:#555}

/* partners */
.partners{left:0;top:1047px;width:786px;height:96px;background:var(--band)}
.partner{top:38px;display:flex;align-items:center;gap:4px;font-family:var(--display);font-weight:700;font-size:18px;color:#3b3fa8}
.partner i{display:block;width:16px;height:16px;border-radius:50%;background:#3b3fa8}
.partner.net{color:#c0392b}
.partner.net i{background:#c0392b}

/* footer */
.site-footer{left:0;top:1143px;width:786px;height:57px;background:var(--ink);color:#e6e6e6;font-size:7px;text-align:center}
.site-footer p{position:absolute;left:0;width:786px}
</style>
</head>
<body>

<header class="site-header abs">
  <span class="brand-mark abs"></span>
  <span class="brand-name abs">StudyAlong</span>
  <div class="brand-tag abs">Knowledge to Boost Your Career</div>
  <nav class="main-nav">
    <a class="active" href="#" style="left:475px">HOME</a>
    <a href="#" style="left:545px">BUY</a>
    <a href="#" style="left:607px">ABOUT</a>
    <a href="#" style="left:679px">CONTACT</a>
  </nav>
</header>

<section class="hero abs">
  <div class="hero-art abs" role="img" aria-label="Illustration of a tree whose crown is made of open books"></div>
  <h1 class="hero-title abs"><span class="l1">KNOWLEDGE</span><span class="l2">TO BOOST YOUR</span><span class="l3">CAREER</span></h1>
</section>

<section class="signup abs">
  <h2>SIGN UP FOR A FREE SAMPLE</h2>
  <div class="field abs" style="left:122px">First Name</div>
  <div class="field abs" style="left:331px">Email Address</div>
  <div class="submit abs">SUBMIT</div>
</section>

<section class="catalog abs">
  <div class="book-panel abs" style="top:41px;height:191px">
    <div class="panel-head">
      <div class="panel-toggle"><svg width="11" height="11" viewBox="0 0 11 11"><circle cx="5.5" cy="5.5" r="5.5" fill="#8a8a8a"/><path d="M5.5 2.5 8.3 5.6H6.6V8.5H4.4V5.6H2.7Z" fill="#fff"/></svg></div>
      <div class="panel-title">VertexJS 1.5 &amp; Strapline</div>
      <div class="app-link"><svg width="9" height="9" viewBox="0 0 9 9" fill="none" stroke="#666" stroke-width="1.2"><rect x="0.8" y="0.8" width="4" height="4" rx="1.5" transform="rotate(45 2.8 2.8)"/><rect x="4.2" y="4.2" width="4" height="4" rx="1.5" transform="rotate(45 6.2 6.2)"/></svg>VIEW APP LINK</div>
    </div>
    <table class="price-table">
      <tr><td>With Mock Services</td><td class="price">$5.99</td><td class="store">Buy from Us<span class="store-dot"></span><span class="store-name">payloop</span></td><td class="store">Buy from<span class="store-name">rivermart</span></td></tr>
      <tr><td>With KnotJS Services</td><td class="price">$5.99</td><td class="store">Buy from Us<span class="store-dot"></span><span class="store-name">payloop</span></td><td class="store">Buy from<span class="store-name">rivermart</span></td></tr>
      <tr><td>With ColdForge Services</td><td class="price">$5.99</td><td class="store">Buy from Us<span class="store-dot"></span><span class="store-name">payloop</span></td><td class="store">Buy from<span class="store-name">rivermart</span></td></tr>
      <tr><td>Buy Them All</td><td class="price">$9.99</td><td class="store">Buy from Us<span class="store-dot"></span><span class="store-name">payloop</span></td><td class="store">Buy from<span class="store-name">rivermart</span></td></tr>
    </table>
  </div>

  <div class="book-panel abs" style="top:243px;height:37px">
    <div class="panel-head">
      <div class="panel-toggle"><svg width="11" height="11" viewBox="0 0 11 11"><circle cx="5.5" cy="5.5" r="5.5" fill="#8a8a8a"/><path d="M5.5 8.5 8.3 5.4H6.6V2.5H4.4V5.4H2.7Z" fill="#fff"/></svg></div>
      <div class="panel-title">VertexJS 2 &amp; Strapline</div>
      <div class="app-link"><svg width="9" height="9" viewBox="0 0 9 9" fill="none" stroke="#666" stroke-width="1.2"><rect x="0.8" y="0.8" width="4" height="4" rx="1.5" transform="rotate(45 2.8 2.8)"/><rect x="4.2" y="4.2" width="4" height="4" rx="1.5" transform="rotate(45 6.2 6.2)"/></svg>VIEW APP LINK</div>
    </div>
  </div>

  <div class="book-panel abs" style="top:292px;height:37px">
    <div class="panel-head">
      <div class="panel-toggle"><svg width="11" height="11" viewBox="0 0 11 11"><circle cx="5.5" cy="5.5" r="5.5" fill="#8a8a8a"/><path d="M5.5 8.5 8.3 5.4H6.6V2.5H4.4V5.4H2.7Z" fill="#fff"/></svg></div>
      <div class="panel-title">ReflexJS</div>
      <div class="app-link"><svg width="9" height="9" viewBox="0 0 9 9" fill="none" stroke="#666" stroke-width="1.2"><rect x="0.8" y="0.8" width="4" height="4" rx="1.5" transform="rotate(45 2.8 2.8)"/><rect x="4.2" y="4.2" width="4" height="4" rx="1.5" transform="rotate(45 6.2 6.2)"/></svg>VIEW APP LINK</div>
    </div>
  </div>
</section>

<section class="author abs">
  <div class="author-photo abs" role="img" aria-label="Portrait photo of the author"></div>
  <h2 class="author-title abs">ABOUT THE AUTHOR</h2>
  <div class="author-copy abs">
    <p>I'm Marlon Trevick and I am a Technical Entrepreneur who likes to do cool things and share them with other people.</p>
    <p>I was the brains behind Gridmora, a set of UI Components for Grid Developers. I produced The Grid Show, a podcast educating Grid Developers about Grid Development. I am also one of the initial members of the Harbor Grid project management committee, as well as a Kiln Community Professional. If you asked a Grid question on QueueSpill, there is a good chance I gave you an answer.</p>
  </div>
</section>

<section class="partners abs">
  <div class="partner abs" style="left:124px"><i></i>PathPastGrid</div>
  <div class="partner abs" style="left:308px"><i></i>Gridmora</div>
  <div class="partner net abs" style="left:475px"><i></i>NetBrookly Consulting</div>
</section>

<footer class="site-footer abs">
  <p style="top:17px">© Copyright 2016 Study Along. All Right Reserved.</p>
  <p style="top:32px">This site is part of the NetBrookly Brain Trust!</p>
</footer>

</body>
</html>
```